Website upgrade

I have two websites linked to the same business. One is for commercial and retail clients the other is for private and residential customers. I need a creative, modern thinking and bold designer to redesign my sites so that they look more professional and eye catching. The two sites are: www.peterhollandltd.com and www.brkfittingworks.com

Target Market(s)

brk fittings targets home owners and individuals who want work done to their property and peter holland targets commercial customers who want shopfitting work undertaken

Industry/Entity Type

Home Improvement

Number of Pages Required

5+ page

Font styles to use
Sans Serif

Colors
0255a3
3176b5
0292cd
85acd3
85cae6

Requirements
Must have
• i want a site to reflect my existing sites but with a bit more of a wow factor to draw customers in
Nice to have
• logo designed, video or slide show
Should not have
• blog page

```html
<!DOCTYPE html>
<html lang="en">
<head>
<meta charset="utf-8">
<title>Peter Holland Contracting Ltd</title>
<link href="https://fonts.googleapis.com/css2?family=Open+Sans:wght@400;600;700&family=Questrial&display=swap" rel="stylesheet">
<style>
:root{
  --navy:#2e4470;
  --title:#2e4068;
  --mist:#e6e6e6;
  --ink:#111;
  --grey:#555;
  --white:#fff;
}
*{box-sizing:border-box;margin:0;padding:0}
html,body{width:729px;height:1200px;overflow:hidden;background:var(--white)}
body{position:relative;font-family:"Open Sans",sans-serif;color:var(--ink)}
.abs{position:absolute}

.masthead{left:0;top:0;width:729px;height:92px;background:var(--mist)}
.wordmark{left:0;top:20px;width:729px;text-align:center;font-family:"Questrial",sans-serif;font-weight:400;font-size:18px;color:var(--title);letter-spacing:1px}
.wordmark-year{left:0;top:44px;width:729px;text-align:center;font-family:"Questrial",sans-serif;font-weight:400;font-size:8px;color:var(--title);letter-spacing:1px}

.hero{left:0;top:91px;width:729px;height:357px;background:linear-gradient(110deg,#5a5a5c 0%,#3c3d42 35%,#2c2e33 60%,#4a4240 85%,#6b5a52 100%)}
.hero-shade{left:0;top:91px;width:729px;height:357px;background:rgba(20,24,34,.35)}

.main-nav{left:28px;top:64px;width:671px;height:54px;background:var(--navy);border-radius:4px;box-shadow:0 2px 4px rgba(0,0,0,.3)}
.main-nav a{position:absolute;top:22px;font-size:9px;font-weight:700;color:var(--white);text-decoration:none;transform:translateX(-50%);letter-spacing:.2px}

.hero-title{left:0;top:195px;width:729px;text-align:center;color:var(--white);font-weight:700;font-size:34px;line-height:35px;letter-spacing:1.5px}
.hero-copy{left:100px;top:277px;width:540px;text-align:center;color:var(--white);font-size:8px;line-height:13.5px}
.btn{display:block;text-align:center;color:var(--white);background:var(--navy);font-size:7px;text-decoration:none;border-radius:3px}
.hero-btn{left:323px;top:322px;width:82px;height:26px;line-height:24px;border:1px solid var(--white)}
.slide-arrows{left:348px;top:430px;width:40px;height:18px;background:#e9e9e9}

.welcome{left:0;top:448px;width:729px;height:177px;background:var(--mist)}
.welcome-title{left:0;top:479px;width:729px;text-align:center;font-family:"Questrial",sans-serif;font-size:18px;font-weight:700;color:var(--ink)}
.welcome-title span{color:var(--navy)}
.welcome-copy{left:82px;top:517px;width:565px;text-align:center;font-size:6.6px;line-height:13.8px;color:var(--grey)}
.welcome-btn{left:325px;top:572px;width:79px;height:24px;line-height:24px}

.section-title{left:0;top:648px;width:729px;text-align:center;font-family:"Questrial",sans-serif;font-size:19px;font-weight:700;color:var(--ink)}
.section-title span{color:var(--navy)}
.service-cards{left:0;top:690px}

.testimonials{left:0;top:956px;width:729px;height:202px;background:var(--navy)}
.testimonials-title{left:0;top:986px;width:729px;text-align:center;font-family:"Questrial",sans-serif;font-size:21px;font-weight:700;color:var(--white)}
.avatar{left:126px;top:1040px;width:50px;height:50px;border-radius:50%;border:2px solid var(--white);background:#b9bfc9}
.quote{left:193px;top:1040px;width:440px;color:var(--white);font-size:7.5px;line-height:17.5px}
.quote-mark{position:absolute;font-family:Georgia,serif;font-size:16px;font-style:italic}
.quote-author{left:500px;top:1080px;width:128px;text-align:right;color:var(--white);font-size:10.5px}
.dots{left:362px;top:1118px;width:46px;height:12px}

.footer{left:0;top:1158px;width:729px;height:42px;background:var(--white)}
.copyright{left:29px;top:1176px;font-size:7px;color:#333}
.social{top:1181px;width:8px;height:8px;border-radius:50%;background:#3a3f4c}
</style>
</head>
<body>

<header class="abs masthead"></header>
<div class="abs wordmark">PETER HOLLAND CONTRACTING LTD</div>
<div class="abs wordmark-year">EST 2004</div>

<div class="abs hero" role="img" aria-label="Photograph of a person working at a laptop showing architectural drawings"></div>
<div class="abs hero-shade"></div>

<nav class="abs main-nav">
  <a href="#" style="left:87px">HOME</a>
  <a href="#" style="left:177px">ABOUT US</a>
  <a href="#" style="left:276px">SERVICES</a>
  <a href="#" style="left:367px">CLIENT</a>
  <a href="#" style="left:471px">TESTIMONIALS</a>
  <a href="#" style="left:581px">CONTACTS</a>
</nav>

<h1 class="abs hero-title">HIGH QUALITY INTERIOR FIT-OUT<br>&amp; REFURBISHMENT SERVICES</h1>
<p class="abs hero-copy">Lorem ipsum dolor sit amet, consectetur adipiscing elit, sed do eiusmod tempor incididunt ut labore et dolore magna aliqua. Ut enim ad minim veniam, quis nostrud exercitation ullamco laboris nisi ut aliquip ex ea commodo consequat.</p>
<a href="#" class="abs btn hero-btn">READ MORE</a>
<svg class="abs slide-arrows" viewBox="0 0 40 18">
  <path d="M16 5 L12 9 L16 13" fill="none" stroke="#222" stroke-width="1.4"/>
  <path d="M25 5 L29 9 L25 13" fill="none" stroke="#222" stroke-width="1.4"/>
</svg>

<section class="abs welcome"></section>
<h2 class="abs welcome-title">Welcome to <span>PETER HOLLAND CONTRACTING LTD</span></h2>
<p class="abs welcome-copy">Peter Holland Contracting provide Project Management &amp; Interior fit-out services to all types of commercial &amp; retail clients. With over 25 years of industry experience, our attention to detail, focus on quality &amp; competitive pricing, ensures repeat business and continued growth with existing clients. If you would like any further information regarding the services that we provide, please do not hesitate to contact us</p>
<a href="#" class="abs btn welcome-btn">READ MORE</a>

<h2 class="abs section-title">Our <span>Service</span></h2>
<svg class="abs service-cards" width="729" height="222" viewBox="0 690 729 222">
  <defs>
    <linearGradient id="property-tone" x1="0" y1="0" x2="0" y2="1">
      <stop offset="0" stop-color="#6f9fd6"/><stop offset=".5" stop-color="#c9a27e"/><stop offset="1" stop-color="#d8b79d"/>
    </linearGradient>
    <linearGradient id="site-tone" x1="0" y1="0" x2="1" y2="1">
      <stop offset="0" stop-color="#d9d9d9"/><stop offset="1" stop-color="#f2f2f2"/>
    </linearGradient>
    <linearGradient id="tower-tone" x1="0" y1="0" x2="0" y2="1">
      <stop offset="0" stop-color="#c5ccd6"/><stop offset=".6" stop-color="#a1968c"/><stop offset="1" stop-color="#7d6b60"/>
    </linearGradient>
  </defs>
  <g role="img" aria-label="Photograph of a model house held in a hand">
    <polygon points="70,693 272,693 230,907 29,907" fill="url(#property-tone)" stroke="#2e4470" stroke-width="1"/>
  </g>
  <g role="img" aria-label="Line drawing of a house plan">
    <polygon points="280,693 485,693 453,907 242,907" fill="url(#site-tone)" stroke="#2e4470" stroke-width="1"/>
  </g>
  <g role="img" aria-label="Photograph of city office towers">
    <polygon points="498,693 698,693 656,907 455,907" fill="url(#tower-tone)" stroke="#2e4470" stroke-width="1"/>
  </g>

  <polygon points="40,850 244,850 236,890 37,890" fill="#2e4470" fill-opacity=".88"/>
  <polygon points="250,850 459,850 455,890 246,890" fill="#2e4470" fill-opacity=".88"/>
  <polygon points="462,850 666,850 660,890 458,890" fill="#2e4470" fill-opacity=".88"/>

  <g font-family="Questrial, sans-serif" fill="#fff" text-anchor="middle">
    <text x="137" y="864" font-size="10.5" font-weight="700">Property Services</text>
    <text x="137" y="877" font-size="8" font-family="Open Sans, sans-serif">Refurbishment, Maintenance &amp; Repairs</text>
    <text x="351" y="864" font-size="10.5" font-weight="700">Site Services</text>
    <text x="351" y="877" font-size="8" font-family="Open Sans, sans-serif">Project &amp; Site Management</text>
    <text x="564" y="864" font-size="10.5" font-weight="700">Contracting (sub-contracting)</text>
    <text x="564" y="877" font-size="8" font-family="Open Sans, sans-serif">Shopfitting &amp; Installation Services</text>
  </g>

  <g stroke="#fff" stroke-width="1.2">
    <circle cx="133" cy="889" r="9" fill="#2e4470"/>
    <circle cx="347" cy="889" r="9" fill="#2e4470"/>
    <circle cx="562" cy="889" r="9" fill="#2e4470"/>
  </g>
  <g fill="none" stroke="#fff" stroke-width="1.6">
    <path d="M131 885 L135 889 L131 893"/>
    <path d="M345 885 L349 889 L345 893"/>
    <path d="M560 885 L564 889 L560 893"/>
  </g>
</svg>

<section class="abs testimonials"></section>
<h2 class="abs testimonials-title">Client Testimonials</h2>
<div class="abs avatar" role="img" aria-label="Portrait photograph of the client"></div>
<p class="abs quote"><span class="quote-mark" style="left:-10px;top:-8px">“</span>Lorem ipsum dolor sit amet, consectetur adipiscing elit, sed do eiusmod tempor incididunt ut labore et dolore magna aliqua. Ut enim ad minim veniam, quis nostrud exercitation ullamco laboris.<span class="quote-mark" style="position:relative;top:2px;left:2px">”</span></p>
<p class="abs quote-author">- Mark Ellison</p>
<svg class="abs dots" viewBox="0 0 46 12">
  <circle cx="9" cy="6" r="3" fill="#fff"/>
  <circle cx="23" cy="6" r="4.5" fill="none" stroke="#fff" stroke-width="1"/>
  <circle cx="23" cy="6" r="2.6" fill="#fff"/>
  <circle cx="37" cy="6" r="3" fill="#fff"/>
</svg>

<footer class="abs footer"></footer>
<p class="abs copyright">All Rights Reserved. Copyrights @company Name. 2016</p>
<span class="abs social" style="left:596px" aria-label="Feed"></span>
<span class="abs social" style="left:620px" aria-label="Social profile"></span>
<span class="abs social" style="left:643px" aria-label="Social profile"></span>
<span class="abs social" style="left:666px" aria-label="Social profile"></span>
<span class="abs social" style="left:689px" aria-label="Social profile"></span>

</body>
</html>
```